A products line website

Design theme: Corporate, elegant, neat, clean and warm and containing the following pages:
1. About Tarvelle lightening collection
2. Side banner(s) in home page for internal promotions, e.g.: New product, new designs, exhibitions, etc.)
3. Product catalogue that could be classified based on two level classification
4. Crystal quality
5. Lightening projects, few words about the lightening project and a link to the special design chandelier projects website
6. Special design chandeliers
a. About Special Design Chandeliers Projects containing:
i. Tarvelle Design dpt.
ii. Safety factors
iii. Artists (designer’s names)
iv. Ability to produce any chandelier size
b. Projects showcase, A study case with detailed photos and videos if possible about successful lightening projects from entire world, classified by type (Hotels, Banks, Religious bldgs...etc.)
c. Interior Design Firms
d. Request a Special Design
7. All the general requirements

Requirements
Must have
• The design should include a home webpage and an internal page design. The design should fullfill the following requriements:

1. Strictly follow the corporate identity materials guidelines - see attachment
2. Supports multi-language
3. User can change between languages using flags
4. Web surfer can optionally change the default language
5. An integrated live chat push button for ChatBrindo
8. Site Header should contain the following information:
a. Logo
b. Slogan
c. Links to site pages
d. Link to the home page
e. Link to the landing page
f. A language option drop box
9. Footers should have:
a. Links to all other 5 websites in a dropbox form
b. Link to privacy statement
c. Link to copyright notice
d. Link to sitemap
e. Newsletter subscription one field form
11. A universal customer service section that offer the following services:
a. Links to end user installation manuals
b. Links to products cleaning and maintenance guide
c. Customer complaints center
12. A news sub-section that should contain:
a. Latest product and promotional announcements
b. Corporate news
c. Exhibitions coverage
13. A link to tarvelle Worldwide:
a. A database driven interactive map reflecting Tarvelle list of agents and distributors worldwide with list of supported products this interactive map could be limited in every sub-site for specific line of product
b. Capture potential resellers and agents
c. Become a partner form

```html
<!DOCTYPE html>
<html lang="en">
<head>
<meta charset="utf-8">
<title>Tarvelle Crystal</title>
<link href="https://fonts.googleapis.com/css2?family=Cabin:wght@400;500&family=PT+Sans:wght@400;700&display=swap" rel="stylesheet">
<style>
:root{
  --page:#2b2427;
  --page-deep:#211b1e;
  --rule:#4a3f44;
  --pink:#d98bab;
  --pink-soft:#e8a9c2;
  --card:#6e4659;
  --card-active:#c98aa5;
  --teal:#2e6f80;
  --teal-dark:#1f4e5c;
  --text:#e9e1e4;
  --muted:#b9adb2;
  --field:#1b1618;
}
*{box-sizing:border-box;margin:0;padding:0}
html,body{width:750px;height:1200px;overflow:hidden;background:var(--page)}
body{position:relative;font-family:"PT Sans",sans-serif;color:var(--text);font-size:11px}
.abs{position:absolute}
.heading{font-family:"Cabin",sans-serif;color:var(--pink);white-space:nowrap}

/* header */
.logo-box{left:38px;top:18px;width:147px;height:104px;background:linear-gradient(#3a3236,#1e191b);border:1px solid #4b4146;border-radius:6px;box-shadow:0 3px 8px rgba(0,0,0,.6);z-index:3;text-align:center}
.logo-box .mark{width:30px;height:30px;border-radius:50%;background:#d9d4d6;margin:20px auto 8px}
.logo-box .name{font-family:"Cabin",sans-serif;font-size:18px;letter-spacing:3px;color:#eee;line-height:20px}
.logo-box .sub{font-size:8px;letter-spacing:5px;color:#ccc}
.login{left:522px;top:0;width:78px;height:22px;background:linear-gradient(#3f8ea3,var(--teal-dark));border-radius:0 0 8px 8px;color:#fff;text-align:center;line-height:22px;font-size:11px}
.live{left:612px;top:12px;width:115px;height:38px;background:linear-gradient(#6b6b6b,#2c2c2c);border-radius:5px;border:1px solid #777}
.live .note{position:absolute;left:32px;top:-3px;font-size:6px;background:#111;color:#eee;padding:0 3px;border-radius:3px;white-space:nowrap}
.live .dot{position:absolute;left:6px;top:8px;width:22px;height:22px;border-radius:50%;background:#ccc}
.live .label{position:absolute;left:35px;top:7px;font-size:13px;color:#fff;white-space:nowrap}
.live .state{position:absolute;left:52px;top:25px;font-size:7px;letter-spacing:1px;color:#f0c94a}
.nav a{position:absolute;top:74px;color:var(--muted);text-decoration:none;font-size:10px;height:16px;line-height:16px;white-space:nowrap}
.nav .home{background:var(--card-active);color:#fff;border-radius:9px;width:52px;text-align:center;border:1px solid #f0c4d5}
.nav-rule{left:195px;top:96px;width:555px;height:1px;background:var(--rule)}
.lang{left:47px;top:128px;font-size:10px;color:#fff;display:flex;gap:4px;align-items:center;z-index:3}
.lang span{display:inline-block;width:19px;height:13px;margin-left:2px}

/* hero */
.hero{left:0;top:97px;width:750px;height:313px;background:
  radial-gradient(ellipse 150px 90px at 255px 135px,rgba(225,225,230,.55),rgba(120,110,120,.25) 60%,transparent 100%),
  radial-gradient(ellipse 110px 120px at 600px 150px,rgba(255,240,215,.6),rgba(190,175,160,.25) 55%,transparent 100%),
  radial-gradient(ellipse 80px 110px at 740px 130px,rgba(230,215,190,.5),transparent 100%),
  linear-gradient(90deg,#8a5a72 0%,#6a4658 22%,#3a3035 48%,#24383f 70%,#2f4047 85%,#5b534e 100%)}
.hero-arrow{top:208px;width:45px;height:45px;background:rgba(70,70,70,.7);border-radius:3px}
.hero-title{left:16px;top:314px;font-family:"Cabin",sans-serif;font-size:22px;letter-spacing:5px;color:rgba(255,255,255,.5);white-space:nowrap}
.hero-caption{left:0;top:347px;width:750px;height:63px;background:rgba(20,16,18,.7);padding:13px 50px 0 24px;font-size:10.5px;line-height:18px;color:#fff}

/* products */
.sec-icon{width:22px;height:22px;border-radius:50%;background:radial-gradient(#fff,#c9c0c4 55%,#6d5560)}
.card{width:95px;height:120px;background:var(--card);border:1px solid #8a6276}
.card.active{background:var(--card-active)}
.card .shot{position:absolute;left:4px;top:4px;width:85px;height:93px}
.card .name{position:absolute;left:5px;top:101px;font-size:8.5px;color:#fff;white-space:nowrap}
.price{position:absolute;left:4px;top:78px;width:85px;height:19px;background:rgba(30,30,30,.8);color:#fff;font-size:8px;line-height:19px;padding-left:4px;white-space:nowrap}
.t-silver{background:radial-gradient(circle at 50% 45%,#d8d8d8,#8d8d8d 55%,#e9e9e9)}
.t-ball{background:radial-gradient(circle at 50% 50%,#f4f6f8,#c9cdd3 45%,#ffffff 70%)}
.t-charm{background:radial-gradient(circle at 55% 55%,#8fa57a,#6b6b6b 45%,#e8e8e8 80%)}
.t-flower{background:radial-gradient(circle at 50% 45%,#a39aa6,#6a6070 40%,#f3f3f3 72%)}
.t-pendant{background:radial-gradient(ellipse at 50% 55%,#b99566,#e9e1d6 50%,#ffffff 75%)}
.t-leaf{background:radial-gradient(circle at 45% 50%,#c7a56a,#3a4356 45%,#1e2433 90%)}
.t-ring{background:radial-gradient(circle at 50% 50%,#bfc3c9,#e6e8eb 45%,#ffffff 75%)}
.t-glass{background:linear-gradient(90deg,#ffffff,#e3e8ec 50%,#ffffff)}
.t-blue{background:radial-gradient(circle at 50% 50%,#ffffff 28%,#3aa6d6 45%,#e9f3f8 70%)}
.t-rose{background:radial-gradient(circle at 50% 60%,#2f9a8e,#3d6b5f 35%,#d9c98a 70%,#efe2a8)}
.t-brooch{background:radial-gradient(circle at 50% 50%,#4d86b0,#b49662 45%,#f6f2ea 75%)}
.t-palm{background:radial-gradient(ellipse at 50% 55%,#a89a8c,#7a5b3e 30%,#f4f2ef 65%)}
.t-belt{background:radial-gradient(circle at 45% 50%,#b9b9b9,#2a2a2a 45%,#111 90%)}
.pager{top:1025px;left:295px;display:flex;gap:5px}
.pager span{height:15px;line-height:14px;background:linear-gradient(#3b8195,var(--teal-dark));border:1px solid #5aa0b3;border-radius:8px;color:#fff;font-size:8.5px;text-align:center;min-width:22px;padding:0 8px}

/* side */
.side-list{left:517px;top:458px;width:203px}
.side-list div{height:27px;line-height:22px;text-align:center;font-size:10px;color:var(--pink-soft);border-bottom:1px solid #4a3e44}
.ad{left:517px;top:643px;width:224px;height:186px;background:#fff;border:1px solid #888}
.ad .brand{position:absolute;left:10px;top:2px;font-family:"PT Sans",sans-serif;font-size:28px;color:#9b2a2f;white-space:nowrap}
.ad .tag{position:absolute;left:112px;top:36px;font-size:9px;color:#333;white-space:nowrap}
.ad .photo{position:absolute;left:45px;top:52px;width:130px;height:115px;background:radial-gradient(circle at 50% 40%,#ffffff,#ece8e2 35%,#b9bcc0 60%,#ffffff 85%)}
.ad .bar{position:absolute;left:2px;bottom:2px;width:218px;height:11px;background:#222;color:#fff;font-size:7.5px;letter-spacing:1.5px;padding-left:4px;line-height:11px;white-space:nowrap}
.news-big{left:517px;top:876px;width:221px;height:78px;background:linear-gradient(#6b4b5d,#2e2529);border:1px solid #b9a3ae;border-radius:5px}
.news-big .icon{position:absolute;left:14px;top:20px;width:38px;height:38px;border-radius:50%;background:#d8d2d5}
.news-big .txt{position:absolute;left:60px;top:6px;width:160px;text-align:center;font-family:"Cabin",sans-serif;font-size:16px;line-height:16px;color:#fff}
.news-btn{left:517px;width:221px;height:29px;background:linear-gradient(#6b4b5d,#3a2e33);border:1px solid #9c8792;border-radius:5px}
.news-btn .sec-icon{position:absolute;left:10px;top:3px}
.news-btn b{position:absolute;left:45px;top:3px;font-family:"Cabin",sans-serif;font-weight:400;font-size:16px;color:var(--pink);white-space:nowrap}

/* footer */
.foot-rule{left:30px;top:1050px;width:690px;height:1px;background:var(--rule)}
.foot-nav{top:1058px;font-size:10px;color:var(--muted);white-space:nowrap}
.foot-band{left:0;top:1075px;width:750px;height:125px;background:radial-gradient(ellipse at 50% 0,#4f3342,var(--page-deep) 70%)}
.foot-title{font-size:11px;color:#fff;white-space:nowrap}
.field{height:22px;background:var(--field);border:1px solid #3e3438;color:#bbb;font-size:9px;line-height:20px;padding-left:7px;white-space:nowrap}
.go{width:26px;height:20px;border-radius:6px;background:linear-gradient(#d891ad,#9b4f71);border:1px solid #e9b9cc;color:#fff;font-size:8.5px;text-align:center;line-height:18px}
.subscribe{left:106px;top:1160px;width:68px;height:15px;border:1px solid #aaa;border-radius:5px;background:linear-gradient(#444,#222);color:#fff;text-align:center;font-size:9.5px;line-height:13px}
.social{top:1133px;width:24px;height:24px;border-radius:50%}
.copy{left:0;top:1173px;width:750px;text-align:center;font-size:8.5px;line-height:11px;color:#fff}
.copy em{font-style:normal;color:#4da6c0}
</style>
</head>
<body>

<!-- header -->
<div class="abs logo-box"><div class="mark"></div><div class="name">TARVELLE</div><div class="sub">CRYSTAL</div></div>
<div class="abs login">Login</div>
<div class="abs live"><span class="note">Please leave a message</span><span class="dot"></span><span class="label">Live Support</span><span class="state">OFFLINE</span></div>
<nav class="nav">
  <a class="home" style="left:205px">Home</a>
  <a style="left:287px">Facilities</a>
  <a style="left:361px">Media Center</a>
  <a style="left:460px">Careers</a>
  <a style="left:541px">About Us</a>
  <a style="left:626px">Contact Us</a>
</nav>
<div class="abs nav-rule"></div>

<!-- hero -->
<div class="abs hero" role="img" aria-label="Crystal-covered jewelry box beside a lit crystal chandelier and a cream sofa"></div>
<div class="abs lang">Language : <span style="background:linear-gradient(#3c3b6e,#3c3b6e) 0 0/8px 7px no-repeat,repeating-linear-gradient(#b22234 0 1px,#fff 1px 2px);margin-left:8px" role="img" aria-label="English flag"></span><span style="background:linear-gradient(90deg,#235 33%,#fff 33% 66%,#c22 66%)" role="img" aria-label="French flag"></span><span style="background:linear-gradient(#111 33%,#c22 33% 66%,#fc0 66%)" role="img" aria-label="German flag"></span></div>
<div class="abs hero-arrow" style="left:15px"><svg width="45" height="45"><path d="M26 15 L18 22.5 L26 30" stroke="#888" stroke-width="3" fill="none"/></svg></div>
<div class="abs hero-arrow" style="left:692px;width:40px;background:rgba(255,255,255,.15)"><svg width="40" height="45"><path d="M16 15 L24 22.5 L16 30" stroke="#ccc" stroke-width="3" fill="none"/></svg></div>
<div class="abs hero-title">TARVELLE CRYSTAL</div>
<div class="abs hero-caption">Lorem Ipsum is simply dummy text of the printing and typesetting industry. Lorem Ipsum has been the industry's standard dummy text ever since the 1500s, when an unknown printer took a galley of type and scrambled it to make a type specimen book.</div>

<!-- products -->
<div class="abs sec-icon" style="left:10px;top:424px"></div>
<div class="abs heading" style="left:45px;top:425px;font-size:18px">Crystal Fashion Components</div>

<div class="abs card active" style="left:47px;top:461px"><div class="shot t-silver" role="img" aria-label="Crystal bow brooch"></div><div class="price">Price : <s>$ 350</s>/- $250</div><div class="name">Product Name</div></div>
<div class="abs card" style="left:151px;top:461px"><div class="shot t-ball" role="img" aria-label="Faceted crystal ball"></div><div class="name">Product Name</div></div>
<div class="abs card" style="left:255px;top:461px"><div class="shot t-charm" role="img" aria-label="Beaded charm bracelet"></div><div class="name">Product Name</div></div>
<div class="abs card" style="left:359px;top:461px"><div class="shot t-flower" role="img" aria-label="Crystal flower brooch"></div><div class="name">Product Name</div></div>

<div class="abs card" style="left:47px;top:601px"><div class="shot t-pendant" role="img" aria-label="Drop pendant necklace"></div><div class="name">Product Name</div></div>
<div class="abs card" style="left:151px;top:601px"><div class="shot t-leaf" role="img" aria-label="Leaf and pearl necklace"></div><div class="name">Product Name</div></div>
<div class="abs card" style="left:255px;top:601px"><div class="shot t-ring" role="img" aria-label="Heart crystal ring"></div><div class="name">Product Name</div></div>
<div class="abs card" style="left:359px;top:601px"><div class="shot t-glass" role="img" aria-label="Pair of crystal glasses"></div><div class="name">Product Name</div></div>

<div class="abs card" style="left:47px;top:741px"><div class="shot t-blue" role="img" aria-label="Blue bead bracelet"></div><div class="name">Product Name</div></div>
<div class="abs card" style="left:151px;top:741px"><div class="shot t-rose" role="img" aria-label="Teal rose bead necklace"></div><div class="name">Product Name</div></div>
<div class="abs card" style="left:255px;top:741px"><div class="shot t-brooch" role="img" aria-label="Blue crystal brooch"></div><div class="name">Product Name</div></div>
<div class="abs card" style="left:359px;top:741px"><div class="shot t-palm" role="img" aria-label="Palm tree crystal brooch"></div><div class="name">Product Name</div></div>

<div class="abs card" style="left:47px;top:882px"><div class="shot t-belt" role="img" aria-label="Studded leather belt"></div><div class="name">Product Name</div></div>
<div class="abs card" style="left:151px;top:882px"><div class="shot t-ring" role="img" aria-label="Heart crystal ring"></div><div class="name">Product Name</div></div>
<div class="abs card" style="left:255px;top:882px"><div class="shot t-rose" role="img" aria-label="Teal rose bead necklace"></div><div class="name">Product Name</div></div>
<div class="abs card" style="left:359px;top:882px"><div class="shot t-leaf" role="img" aria-label="Leaf and pearl necklace"></div><div class="name">Product Name</div></div>

<div class="abs pager"><span>Prev</span><span>2</span><span>3</span><span>4</span><span>Next</span></div>

<!-- side column -->
<div class="abs sec-icon" style="left:534px;top:421px"></div>
<div class="abs heading" style="left:567px;top:421px;font-size:18px">New product</div>
<div class="abs side-list">
  <div>Crystal Fashion Components</div>
  <div>Chandeliers Crystal Parts</div>
  <div>Lighting Collection</div>
  <div>Special design</div>
  <div>Gifts and accessories</div>
</div>

<div class="abs sec-icon" style="left:534px;top:606px"></div>
<div class="abs heading" style="left:567px;top:606px;font-size:18px">Exhibitions</div>
<div class="abs ad"><div class="brand">PearlLane.com</div><div class="tag">Just Pay $5.99 S&amp;P</div><div class="photo" role="img" aria-label="Pearl ring with crystal setting"></div><div class="bar">100s of Freshwater Pearl Styles</div></div>

<div class="abs sec-icon" style="left:528px;top:846px"></div>
<div class="abs heading" style="left:566px;top:846px;font-size:17px">A news sub-section</div>
<div class="abs news-big"><div class="icon" role="img" aria-label="Megaphone icon"></div><div class="txt">Latest Product<br>&amp;<br>Promotional<br>Announcements</div></div>
<div class="abs news-btn" style="top:963px"><span class="sec-icon"></span><b>Corporate News</b></div>
<div class="abs news-btn" style="top:999px"><span class="sec-icon"></span><b>Exhibitions coverage</b></div>

<!-- footer -->
<div class="abs foot-rule"></div>
<div class="abs foot-band"></div>
<div class="abs foot-nav" style="left:103px;color:#fff">Home</div>
<div class="abs foot-nav" style="left:172px">Facilities</div>
<div class="abs foot-nav" style="left:247px">Media Center</div>
<div class="abs foot-nav" style="left:346px">Careers</div>
<div class="abs foot-nav" style="left:427px">About Us</div>
<div class="abs foot-nav" style="left:512px">Contact Us</div>
<div class="abs foot-nav" style="left:601px">Sitemap</div>

<div class="abs foot-title" style="left:51px;top:1103px">News Letter</div>
<div class="abs field" style="left:22px;top:1131px;width:158px">Subscribe news letter</div>
<div class="abs subscribe">Subscribe</div>

<div class="abs foot-title" style="left:214px;top:1101px">Tarvelle Crystal Websites</div>
<div class="abs field" style="left:191px;top:1131px;width:157px;color:var(--pink)">www.tarvellecrystal.com<svg class="abs" style="right:7px;top:7px" width="9" height="7"><path d="M0 0h9L4.5 7z" fill="var(--pink)"/></svg></div>
<div class="abs go" style="left:355px;top:1132px">GO</div>

<div class="abs foot-title" style="left:436px;top:1099px">Partner with us</div>
<div class="abs field" style="left:421px;top:1122px;width:104px">Email id</div>
<div class="abs field" style="left:421px;top:1145px;width:104px">Password</div>
<div class="abs go" style="left:535px;top:1145px">GO</div>

<div class="abs foot-title" style="left:614px;top:1104px">Connect with us</div>
<div class="abs social" style="left:610px;background:#3b5998"></div>
<div class="abs social" style="left:640px;background:#33a6d8"></div>
<div class="abs social" style="left:672px;background:#555"></div>
<div class="abs social" style="left:704px;background:#e8801f"></div>

<div class="abs copy">Copyright © 2011. <em>www.tarvellecrystal.com</em><br>Terms and Conditions - Privacy Policy</div>

</body>
</html>
```